International Petrochemical business needs a web design for Tessaro Desk system

We need a web design for a "Tessaro Desk" system for an international petrochemical company. The web site is used internally within the company. It is hosted by an internal department which provides government permit request service for other departments.

We would like to see designs of two pages using color light blue. (home page, internal page as attached).
Home Page:
1. Header has a background image and small animation. Header on home page can be taller than the header of the internal page.
2. Layout as attached.

Internal Page:
1. Header can use the same background image as the home page and can be shorter to utilize the page for content.
2. The blue icon behind every captions represent an icon. When user move mouse over this icon, it displays the caption in Thai language as a tooltip. This icon needs to be redesign.

The final design should communicate the followings:
- Excellent service provided system in terms of time and accurary
- Rapid growth of business via building petrochemical refinery plant

For Internal Page, the blue circle behind every captions represent an icon. When mouse over this icon, a tool tip showing the caption in Thai language is shown. Please also design this icon..

There are more feedbacks from customer as followed:

1. Banner should consists of 
    1.1 "Approved" stamp on paper
    1.2 An image of Garuda. It is used on every government documents in Thailand
    1.3 Image of petrochemical plant
2. Each menu item (Home, Permit, Search, etc) should have different colors. Drop down menu will use the same color as its parent menu item.
3. Overall tone of the web page should be light blue with background of the body the web page in white
4. "New Request" button should use green color with icon on it
5. Table header of each box in the body of the page should use dark blue background with text in white

Please kindly submit your revisions.
Thank you.

Reason: We get some late feedbacks from customers which was just updated to all designers.

• 1. Design for 1024x768 screen resolution
2. Use light blue theme
3. Background of header where the company logo is must have white background

```html
<!DOCTYPE html>
<html lang="en">
<head>
<meta charset="utf-8">
<title>Tessaro Desk</title>
<link href="https://fonts.googleapis.com/css2?family=Open+Sans:wght@400;600;700&display=swap" rel="stylesheet">
<style>
  :root {
    --page-bg: #eceef0;
    --panel-bg: #ffffff;
    --panel-border: #dcdfe3;
    --rule: #e6e8eb;
    --ink: #4a4f55;
    --ink-soft: #8a9097;
    --ink-faint: #a9aeb4;
    --link: #2c8fd0;
    --accent: #2a93d5;
    --accent-dark: #1f7fbd;
    --dot: #c9ced3;
    --footer-bg: #e4e6e8;
  }
  * { box-sizing: border-box; margin: 0; padding: 0; }
  html, body { width: 880px; height: 1200px; overflow: hidden; }
  body {
    font-family: "Open Sans", Arial, sans-serif;
    color: var(--ink);
    background: var(--page-bg);
    position: relative;
  }

  .hero {
    position: absolute; left: 0; top: 0; width: 880px; height: 252px;
    background:
      linear-gradient(180deg, rgba(20,30,48,0.15) 0%, rgba(20,30,48,0) 40%),
      radial-gradient(ellipse at 62% 78%, #f2a24a 0%, #c8743a 18%, rgba(120,70,50,0) 45%),
      linear-gradient(180deg, #3a4a62 0%, #5b6478 38%, #a9835e 62%, #3a3430 82%, #1d1c1f 100%);
  }
  .site-name {
    position: absolute; left: 32px; top: 20px;
    background: #fff; padding: 7px 14px; border-radius: 2px;
    font-size: 13px; font-weight: 400; color: var(--ink);
  }

  .main-nav {
    position: absolute; left: 50px; top: 252px; width: 780px; height: 28px;
    background: #fff; display: flex; border-bottom: 1px solid var(--panel-border);
  }
  .main-nav a {
    display: block; padding: 0 14px; line-height: 28px; font-size: 11px;
    color: var(--ink); text-decoration: none; border-right: 1px solid var(--rule);
  }
  .main-nav a.active { background: #f2f4f6; }
  .dropdown {
    position: absolute; left: 108px; top: 280px; width: 172px;
    background: #fff; border: 1px solid var(--panel-border); z-index: 2;
  }
  .dropdown a {
    display: block; font-size: 9px; line-height: 18px; padding: 0 10px;
    color: var(--ink); text-decoration: none; border-bottom: 1px solid var(--rule);
  }

  .panel {
    position: absolute; background: var(--panel-bg);
    border: 1px solid var(--panel-border); padding: 14px 16px 0;
  }
  .panel h2 { font-size: 15px; font-weight: 400; color: var(--ink); margin-bottom: 12px; }
  .data-table { width: 100%; border-collapse: collapse; }
  .data-table th {
    font-size: 8px; font-weight: 600; text-transform: uppercase; text-align: left;
    color: var(--ink); padding: 0 4px 4px 0; border-bottom: 1px solid var(--rule);
  }
  .data-table td { font-size: 9.5px; color: var(--ink-soft); padding: 4px 4px 2px 0; }
  .data-table td a { color: var(--link); text-decoration: none; }
  .pager { position: absolute; right: 16px; bottom: 12px; display: flex; gap: 5px; }
  .pager span { width: 6px; height: 6px; border-radius: 50%; background: var(--dot); }
  .pager span.on { background: var(--accent); }

  .new-request-btn {
    position: absolute; left: 445px; top: 720px; width: 385px; height: 60px;
    background: var(--accent); color: #fff; font-size: 20px; font-weight: 600;
    display: flex; align-items: center; justify-content: center; letter-spacing: .5px;
    border-bottom: 3px solid var(--accent-dark); text-decoration: none;
  }

  .site-footer {
    position: absolute; left: 0; top: 940px; width: 880px; height: 260px;
    background: var(--footer-bg);
  }
  .footer-nav {
    display: flex; justify-content: center; gap: 26px; padding-top: 24px;
    font-size: 9px; color: var(--ink-soft);
  }
  .footer-cols { display: flex; gap: 30px; margin: 30px 50px 0; }
  .footer-about { width: 150px; }
  .footer-about .footer-name { font-size: 9px; color: #5d636a; margin-bottom: 10px; }
  .footer-about p { font-size: 8px; color: var(--ink-faint); line-height: 12px; }
  .footer-list { list-style: none; width: 150px; }
  .footer-list li { font-size: 8px; color: var(--ink-faint); line-height: 13px; }
  .copyright {
    position: absolute; left: 50px; right: 50px; bottom: 36px; padding-top: 12px;
    border-top: 1px solid #d3d6d9; text-align: center; font-size: 8px; color: var(--ink-soft);
  }
</style>
</head>
<body>

<header class="hero" role="img" aria-label="Petrochemical refinery plant at dusk with lit towers and pipework">
  <div class="site-name">Norvale Works</div>
</header>

<nav class="main-nav">
  <a href="#">Home</a>
  <a href="#" class="active">Permits</a>
  <a href="#">Search</a>
  <a href="#">Report</a>
  <a href="#">Admin</a>
  <a href="#">Help</a>
</nav>
<div class="dropdown">
  <a href="#">Create New Permit</a>
  <a href="#">Transfer Permit</a>
  <a href="#">Renew Permit</a>
</div>

<section class="panel" style="left:50px; top:296px; width:385px; height:212px;">
  <h2>New Requests</h2>
  <table class="data-table">
    <tr><th>Request No.</th><th>Request Date</th><th>Branch</th></tr>
    <tr><td><a href="#">56-0003</a></td><td>20.04.2013</td><td>BC1</td></tr>
    <tr><td><a href="#">56-0004</a></td><td>21.04.2013</td><td>BC2</td></tr>
  </table>
  <div class="pager"><span class="on"></span><span></span><span></span><span></span></div>
</section>

<section class="panel" style="left:445px; top:296px; width:385px; height:212px;">
  <h2>My Working Requests</h2>
  <table class="data-table">
    <tr><th>Request No.</th><th>Request Date</th><th>Status</th></tr>
    <tr><td><a href="#">55-0209</a></td><td>25.03.2013</td><td>Waiting for process</td></tr>
    <tr><td><a href="#">55-0210</a></td><td>24.03.2013</td><td>In progress</td></tr>
    <tr><td><a href="#">55-0300</a></td><td>18.12.2013</td><td>Incomplete document</td></tr>
    <tr><td><a href="#">55-0301</a></td><td>18.01.2013</td><td>Cancel request</td></tr>
  </table>
  <div class="pager"><span class="on"></span><span></span><span></span><span></span></div>
</section>

<section class="panel" style="left:50px; top:540px; width:780px; height:160px;">
  <h2>Expiring Permits</h2>
  <table class="data-table">
    <tr><th>Permit No.</th><th>Expire Date</th><th>Permit Name</th><th>Branch</th><th>Required Time (Day)</th><th>Due Date</th></tr>
    <tr><td><a href="#">AB56001</a></td><td>25.03.2013</td><td>Permit Name #4410</td><td>BC3</td><td>30</td><td>-10</td></tr>
    <tr><td><a href="#">BK01002</a></td><td>24.03.2013</td><td>Permit Name #4420</td><td>BC3</td><td>60</td><td>15</td></tr>
  </table>
  <div class="pager"><span class="on"></span><span></span><span></span><span></span></div>
</section>

<section class="panel" style="left:50px; top:720px; width:385px; height:200px;">
  <h2>My In Progress Requests</h2>
  <table class="data-table">
    <tr><th>Request No.</th><th>Request Date</th><th>Status</th></tr>
    <tr><td><a href="#">56-0001</a></td><td>20.04.2013</td><td>In review</td></tr>
    <tr><td><a href="#">56-0002</a></td><td>21.04.2013</td><td>Submitted</td></tr>
  </table>
  <div class="pager"><span class="on"></span><span></span><span></span><span></span></div>
</section>

<a class="new-request-btn" href="#">NEW REQUEST</a>

<section class="panel" style="left:445px; top:792px; width:385px; height:128px;">
  <h2>Recent Completed Requests</h2>
  <table class="data-table">
    <tr><th>Request No.</th><th>Completed Date</th></tr>
    <tr><td><a href="#">55-0100</a></td><td>25.03.2013</td></tr>
    <tr><td><a href="#">55-0288</a></td><td>24.03.2013</td></tr>
    <tr><td><a href="#">55-0002</a></td><td>18.12.2013</td></tr>
  </table>
  <div class="pager"><span class="on"></span><span></span><span></span><span></span></div>
</section>

<footer class="site-footer">
  <nav class="footer-nav">
    <span>Home</span><span>Permits</span><span>Search</span><span>Report</span><span>Admin</span><span>Help</span>
  </nav>
  <div class="footer-cols">
    <div class="footer-about">
      <div class="footer-name">Norvale Works</div>
      <p>Short note about the permit office team.</p>
    </div>
    <ul class="footer-list">
      <li>Permit office hours today</li>
      <li>Submit forms before noon</li>
      <li>Check status each morning</li>
      <li>Contact your branch clerk</li>
      <li>Keep copies of receipts</li>
    </ul>
    <ul class="footer-list">
      <li>Renewal rules for branches</li>
      <li>Common permit form guide</li>
      <li>Document checklist for requests</li>
      <li>Review times by type</li>
      <li>Frequently asked staff questions</li>
    </ul>
    <ul class="footer-list">
      <li>Report a system problem</li>
      <li>Request new user access</li>
      <li>Update your branch details</li>
      <li>Training sessions this month</li>
      <li>Send feedback to admin</li>
    </ul>
  </div>
  <div class="copyright">Copyright Norvale Works 2013. All rights reserved.</div>
</footer>

</body>
</html>
```